Home Health Company Needs a Corporate Identity Package

We need a corporate identity package (see what it should include below) for a home health care company. The design should be professional, uncluttered, simple and created in Publisher (so that we can edit the design in the future, if necessary. )
We need the following created:
-Presentation folder
-Business card template (color, double sided)
-Letterhead
-Stationary
-postcard sized marketing piece (5.5" x 8.5", color, double sided)

Target Market(s)

We are in the business of supplying personal care aids for in home care. Our services are directed towards older, retired individuals with some disability or illness. However, we will be marketing to the children or relatives of our in home clients. We want our logo to emphasize our reliability and personalized services.

Industry/Entity Type

Home Health Care

Requirements
Must have
• The design should be professional, uncluttered, simple and created in Publisher (so that we can edit the design in the future, if necessary. )

```html
<!DOCTYPE html>
<html lang="en">
<head>
<meta charset="utf-8">
<title>Harbor Home Care — Stationery Set</title>
<link rel="stylesheet" href="https://fonts.googleapis.com/css2?family=Open+Sans:wght@400;600;700&display=swap">
<style>
  :root{
    --bg:#eeeeee;
    --paper:#ffffff;
    --ink:#222222;
    --charcoal:#2b2b2b;
    --charcoal-dark:#1c1c1c;
    --charcoal-light:#4a4a4a;
    --brand:#3fb4e0;
    --brand-faint:#e3f3fa;
    --rule:#2f7fc4;
    --grey-text:#555555;
  }
  *{box-sizing:border-box;margin:0;padding:0}
  html,body{width:1200px;height:1000px;overflow:hidden}
  body{background:var(--bg);font-family:"Open Sans",Arial,sans-serif;color:var(--ink);position:relative}

  .piece{position:absolute;overflow:hidden}

  /* Brand lockup: stacked name beside a plain dot */
  .brand-name{font-family:"Open Sans",Arial,sans-serif;font-weight:700;color:var(--brand);line-height:1;display:flex;align-items:center;gap:.3em;white-space:nowrap}
  .brand-name .dot{width:.6em;height:.6em;border-radius:50%;background:var(--brand);flex:none}
  .brand-name .words span{display:block}

  .rule{position:absolute;left:0;right:0;height:2px;background:linear-gradient(90deg,var(--rule),var(--rule) 60%,rgba(47,127,196,0))}
  .address{position:absolute;left:0;right:0;text-align:center;font-size:6px;font-weight:600;color:var(--ink)}

  /* Letterhead */
  .letterhead{left:290px;top:95px;width:295px;height:425px;background:var(--paper)}
  .letterhead .logo{position:absolute;left:36px;top:18px;font-size:14px}
  .letterhead .watermark{position:absolute;left:96px;top:172px;font-size:34px;font-weight:700;line-height:1;color:var(--brand-faint)}
  .letterhead .watermark span{display:block}
  .letter-body{position:absolute;left:30px;top:110px;width:250px;font-size:5px;line-height:1.35;color:#111}
  .letter-body p{margin-bottom:5px}
  .letterhead .rule{top:415px}
  .letterhead .address{top:405px}

  /* Folder */
  .folder{left:633px;top:78px;width:350px;height:447px;background:linear-gradient(135deg,var(--charcoal-light),var(--charcoal) 45%,var(--charcoal-dark));display:flex;align-items:center;justify-content:center}
  .folder .brand-name{font-size:40px}

  /* Business cards: content laid out upright, then turned */
  .card{width:136px;height:82px}
  .card-inner{position:absolute;left:27px;top:-27px;width:82px;height:136px}
  .card-front{left:183px;top:549px;background:var(--charcoal)}
  .card-front .card-inner{transform:rotate(-90deg);display:flex;align-items:center;justify-content:center}
  .card-front .brand-name{font-size:12px}
  .card-back{left:183px;top:643px;background:var(--paper)}
  .card-back .card-inner{transform:rotate(90deg);padding:8px 6px}
  .card-back .brand-name{position:absolute;left:8px;bottom:8px;font-size:10px}
  .card-details{font-size:4.5px;color:var(--grey-text);line-height:1.2}
  .card-details .name{font-size:6px;color:var(--ink);font-weight:600}
  .card-details .line{display:flex;gap:3px;align-items:center;margin-top:2px}
  .card-details .line span:first-child{width:14px}
  .card-details .line span:last-child{flex:1;height:2px;background:#777}

  /* Envelope front */
  .envelope-front{left:350px;top:557px;width:340px;height:164px;background:linear-gradient(180deg,#f7f7f7,#ffffff)}
  .envelope-front .brand-name{position:absolute;left:250px;top:16px;font-size:11px}
  .envelope-front .address{top:142px}
  .envelope-front .rule{top:152px}

  /* Envelope back */
  .envelope-back{left:708px;top:557px;width:333px;height:164px;background:var(--paper)}
  .envelope-back .flap{position:absolute;left:0;top:0;width:333px;height:46px}
  .envelope-back .brand-name{position:absolute;left:138px;top:8px;font-size:10px}
  .envelope-back .rule{top:152px}

  /* CD sleeve */
  .cd-sleeve{left:243px;top:770px;width:195px;height:180px;background:linear-gradient(135deg,var(--charcoal-light),var(--charcoal-dark));display:flex;align-items:center;justify-content:center}
  .cd-sleeve .brand-name{font-size:24px}

  /* Disc */
  .disc{left:470px;top:768px;width:148px;height:148px}
  .disc .brand-name{position:absolute;left:56px;top:12px;font-size:10px}

  /* Compliments slip */
  .compliments{left:733px;top:763px;width:322px;height:153px;background:linear-gradient(90deg,#ffffff,#f4f4f4)}
  .compliments .brand-block{position:absolute;left:0;top:0;width:138px;height:80px;background:var(--charcoal);display:flex;align-items:center;justify-content:center}
  .compliments .brand-name{font-size:17px}
  .compliments .arc{position:absolute;left:205px;top:10px}
  .compliments .headline{position:absolute;left:18px;top:106px;font-size:12px;font-weight:600;letter-spacing:.3px;color:#333}
  .compliments .slip-address{position:absolute;left:18px;top:121px;font-size:6.5px;font-weight:600;color:var(--grey-text);line-height:1.35}
  .compliments .rule{top:143px;left:0;right:130px}
</style>
</head>
<body>

  <section class="piece letterhead">
    <div class="brand-name logo"><span class="dot"></span><span class="words"><span>Harbor</span><span>Home</span><span>Care</span></span></div>
    <div class="watermark" aria-hidden="true"><span>Harbor</span><span>Home</span><span>Care</span></div>
    <div class="letter-body">
      <p>72 Maple Court<br>Riverton, CA 90000.</p>
      <p>January 29th, 2011</p>
      <p>Mr. Dalton<br>President, Dalton Family Center<br>18 Orchard Road<br>Brookvale, NY 10000</p>
      <p>Dear Mr. Dalton:</p>
      <p>In the first paragraph, one needs to give a brief introduction of oneself. One should also give reference to the purpose of the letter in brief.<br>The second paragraph needs to give the details of the letter and its need. This paragraph is mostly longer than the others and plays the main role in the letter. Keep the sentences short and to the point. Avoid using complex words and sentences.</p>
      <p style="margin-top:12px">The third and last paragraph is the conclusion of the letter and can be kept short.</p>
      <p>Sincerely,</p>
      <p>(this is where the signature of the writer will be placed)</p>
      <p>Jordan Hale<br>Read more at: www.letterguide-sample.com/formats</p>
    </div>
    <div class="address">410 Lantern Avenue, Suite 220, Fairview, FL 32000 | 800.555.0142</div>
    <div class="rule"></div>
  </section>

  <section class="piece folder">
    <div class="brand-name"><span class="dot"></span><span class="words"><span>Harbor</span><span>Home</span><span>Care</span></span></div>
  </section>

  <section class="piece card card-front">
    <div class="card-inner">
      <div class="brand-name"><span class="dot"></span><span class="words"><span>Harbor</span><span>Home</span><span>Care</span></span></div>
    </div>
  </section>

  <section class="piece card card-back">
    <div class="card-inner">
      <div class="card-details">
        <div class="name">Your Name</div>
        <div>Position</div>
        <div class="line"><span>Address</span><span></span></div>
        <div class="line"><span>Phone</span><span></span></div>
        <div class="line"><span>Fax</span><span></span></div>
        <div class="line"><span>Web</span><span></span></div>
      </div>
      <div class="brand-name"><span class="dot"></span><span class="words"><span>Harbor</span><span>Home</span><span>Care</span></span></div>
    </div>
  </section>

  <section class="piece envelope-front">
    <div class="brand-name"><span class="dot"></span><span class="words"><span>Harbor</span><span>Home</span><span>Care</span></span></div>
    <div class="address">410 Lantern Avenue, Suite 220, Fairview, FL 32000 | 800.555.0142</div>
    <div class="rule"></div>
  </section>

  <section class="piece envelope-back">
    <svg class="flap" viewBox="0 0 333 46" preserveAspectRatio="none">
      <polygon points="0,0 333,0 325,46 8,46" fill="#2b2b2b"/>
    </svg>
    <div class="brand-name"><span class="dot"></span><span class="words"><span>Harbor</span><span>Home</span><span>Care</span></span></div>
    <div class="rule"></div>
  </section>

  <section class="piece cd-sleeve">
    <div class="brand-name"><span class="dot"></span><span class="words"><span>Harbor</span><span>Home</span><span>Care</span></span></div>
  </section>

  <section class="piece disc">
    <svg width="148" height="148" viewBox="0 0 148 148">
      <defs>
        <radialGradient id="disc-shade" cx="50%" cy="50%" r="50%">
          <stop offset="0" stop-color="#9a9a9a"/>
          <stop offset="1" stop-color="#2a2a2a"/>
        </radialGradient>
      </defs>
      <circle cx="74" cy="74" r="73" fill="url(#disc-shade)"/>
      <circle cx="74" cy="74" r="22" fill="#cfcfcf"/>
      <circle cx="74" cy="74" r="9" fill="#eeeeee"/>
    </svg>
    <div class="brand-name"><span class="dot"></span><span class="words"><span>Harbor</span><span>Home</span><span>Care</span></span></div>
  </section>

  <section class="piece compliments">
    <div class="brand-block">
      <div class="brand-name"><span class="dot"></span><span class="words"><span>Harbor</span><span>Home</span><span>Care</span></span></div>
    </div>
    <svg class="arc" width="170" height="170" viewBox="0 0 170 170">
      <circle cx="85" cy="85" r="75" fill="none" stroke="#d7eef8" stroke-width="12"/>
    </svg>
    <div class="headline">WITH COMPLIMENTS</div>
    <div class="slip-address">410 Lantern Avenue, Suite 220, Fairview,<br>FL 32000 | 800.555.0142</div>
    <div class="rule"></div>
  </section>

</body>
</html>
```